Letterhead, envelope & business card design

We would like to refresh the look and feel of our business cards & letterheads.

Our company specialises in premium property.

We are looking for a unique minimalist design for our letterhead & business cards that project this.

I can send over examples of our current design to draw from, although Im looking for some one with creativity, yet focussed on a clean modern, minimalist design.
Updates

I have just uploaded our current letterhead.

We have just removed the 'swoosh' grey symbol, but would still like to keep some part of grey in the design if possible.

thanks in advance.

Just uploaded my details for business card.

Can we see examples with the light grey used as the secondary color?

thanks in advance.

Target Market(s)

We are a premium real estate agency & we want that message to be carried through our business cards & stationery.

Industry/Entity Type

Business

```html
<!DOCTYPE html>
<html lang="en">
<head>
<meta charset="utf-8">
<title>Hartwell Estate Agents – Stationery</title>
<link rel="stylesheet" href="https://fonts.googleapis.com/css2?family=Source+Sans+3:wght@400;600;700&display=swap">
<style>
  :root {
    --ink: #0b3a4e;
    --text: #3a3f44;
    --mist: #e9eaee;
    --paper: #ffffff;
    --edge: #9a9ea3;
    --font: "Source Sans 3", "Helvetica Neue", Arial, sans-serif;
  }
  * { margin: 0; padding: 0; box-sizing: border-box; }
  html, body { width: 1200px; height: 900px; overflow: hidden; background: var(--paper); }
  body { position: relative; font-family: var(--font); color: var(--text); }

  /* Letterhead */
  .letterhead {
    position: absolute; left: 430px; top: 35px; width: 586px; height: 828px;
    background: var(--paper); border: 1px solid var(--edge);
    box-shadow: 1px 2px 3px rgba(0,0,0,.18);
  }
  .letterhead__bar { position: absolute; right: 0; top: 0; width: 14px; height: 100%; background: var(--ink); }
  .letterhead__brand {
    position: absolute; left: 27px; top: 84px;
    font-size: 21px; font-weight: 600; color: var(--ink); letter-spacing: .3px;
  }
  .letterhead__contact {
    position: absolute; right: 27px; top: 26px; text-align: right;
    font-size: 7.6px; line-height: 1.35; color: var(--text);
  }
  .letterhead__contact .company { font-weight: 700; color: var(--ink); font-size: 8.6px; }
  .letterhead__contact p + p { margin-top: 5px; }
  .letterhead__contact b { color: var(--ink); }
  .letterhead__watermark { position: absolute; left: 465px; top: 105px; width: 110px; height: 700px; }

  /* Business cards */
  .card {
    position: absolute; left: 313px; width: 246px; height: 153px;
    border-radius: 6px; overflow: hidden; background: var(--paper);
    border: 1px solid var(--edge); box-shadow: 1px 2px 3px rgba(0,0,0,.2);
  }
  .card--front { top: 433px; }
  .card--back { top: 601px; }

  .card--front .card__field {
    position: absolute; left: 0; top: 0; width: 100%; height: 133px; background: var(--ink);
    display: flex; align-items: center; justify-content: center;
  }
  .card__brand { color: var(--paper); font-size: 19px; font-weight: 600; letter-spacing: .3px; }
  .card__web {
    position: absolute; left: 0; bottom: 0; width: 100%; height: 20px;
    display: flex; align-items: center; justify-content: center;
    font-size: 8.4px; font-weight: 700; color: var(--ink);
  }

  .card__details { position: absolute; left: 20px; top: 33px; font-size: 7.6px; line-height: 1.3; }
  .card__name { font-size: 8.8px; font-weight: 700; color: var(--ink); }
  .card__phones { margin-top: 10px; }
  .card__phones b { color: var(--ink); }
  .card__watermark { position: absolute; left: 224px; top: 12px; width: 22px; height: 118px; }
  .card__address {
    position: absolute; left: 0; bottom: 0; width: 100%; height: 20px; background: var(--ink);
    display: flex; align-items: center; justify-content: center;
    font-size: 8.4px; color: var(--paper);
  }
</style>
</head>
<body>

<section class="letterhead">
  <div class="letterhead__brand">Hartwell Estate Agents</div>
  <div class="letterhead__contact">
    <p class="company">Hartwell Estate Agents<br><span style="font-weight:400;color:var(--text);font-size:7.6px">ABN: 47 318 205 962</span></p>
    <p>128 Shore Road, Bayview NSW 2260</p>
    <p><b>P:</b> 02 4381 5520 | <b>M:</b> 0412 507 936<br><b>E:</b> info@hartwellestates.com.au | <b>W:</b> www.hartwellestates.com.au</p>
  </div>
  <svg class="letterhead__watermark" viewBox="0 0 110 700" aria-hidden="true">
    <text x="0" y="0" transform="translate(102 700) rotate(-90)" textLength="700" lengthAdjust="spacingAndGlyphs"
          font-family="Source Sans 3, Arial, sans-serif" font-size="138" font-weight="400" fill="#e9eaee">HARTWELL</text>
  </svg>
  <div class="letterhead__bar"></div>
</section>

<section class="card card--front">
  <div class="card__field"><span class="card__brand">Hartwell Estate Agents</span></div>
  <div class="card__web">www.hartwellestates.com.au</div>
</section>

<section class="card card--back">
  <div class="card__details">
    <p class="card__name">Neil Hartwell</p>
    <p>Director | Hartwell Estate Agents</p>
    <p>Registered Valuer 021 583</p>
    <p class="card__phones"><b>P:</b> 02 4381 5520<br><b>M:</b> 0412 507 936<br><b>E:</b> info@hartwellestates.com.au</p>
  </div>
  <svg class="card__watermark" viewBox="0 0 22 118" aria-hidden="true">
    <text x="0" y="0" transform="translate(20 118) rotate(-90)" textLength="118" lengthAdjust="spacingAndGlyphs"
          font-family="Source Sans 3, Arial, sans-serif" font-size="24" fill="#e9eaee">HARTWELL</text>
  </svg>
  <div class="card__address">128 Shore Rd, Bayview NSW 2260</div>
</section>

</body>
</html>
```